Rocket business card

Modern business card design, use of color is good with clean space too.

Things to include on card:

Quote: I add fuel to your optometry practice

- Eyewear Sales
- Admin Duties
- Revenue Collection
- Leadership
- Tech Adoption
- COGS Reduction
- Product Sourcing
-Medical Growth

Dalton Vessey, CEO
Glint Harbor
Text Me! 847-302-1964
dalton@glintharbor.example

```html
<!DOCTYPE html>
<html lang="en">
<head>
<meta charset="utf-8">
<title>Glint Harbor – Business Card</title>
<link href="https://fonts.googleapis.com/css2?family=Oswald:wght@500;600&family=Roboto:wght@400;500&display=swap" rel="stylesheet">
<style>
  :root {
    --page-bg: #d9d9d9;
    --card-bg: #0b0b0c;
    --card-edge: #c0560f;
    --accent: #f28a1e;
    --text-light: #f2f2f2;
    --divider: #5a5a5a;
  }
  * { box-sizing: border-box; margin: 0; padding: 0; }
  html, body {
    width: 1200px;
    height: 800px;
    overflow: hidden;
  }
  body {
    background: var(--page-bg);
    display: flex;
    align-items: center;
    justify-content: center;
    gap: 32px;
    font-family: "Roboto", Arial, sans-serif;
  }
  .card {
    width: 560px;
    height: 320px;
    background: var(--card-bg);
    border-bottom: 3px solid var(--card-edge);
    box-shadow: 0 10px 24px rgba(0,0,0,0.25);
    position: relative;
    color: var(--text-light);
  }

  /* Info side */
  .card-info { padding: 70px 40px 0 70px; }
  .identity-row {
    display: flex;
    align-items: center;
  }
  .identity {
    text-align: right;
    padding-right: 18px;
  }
  .identity-name {
    font-family: "Oswald", "Arial Narrow", sans-serif;
    font-weight: 600;
    font-size: 30px;
    line-height: 1;
    color: var(--accent);
    letter-spacing: 0.5px;
    text-transform: uppercase;
  }
  .identity-title {
    font-family: "Oswald", "Arial Narrow", sans-serif;
    font-weight: 600;
    font-size: 17px;
    line-height: 1.1;
    color: var(--text-light);
  }
  .divider {
    width: 1px;
    height: 66px;
    background: var(--divider);
  }
  .contact-list {
    list-style: none;
    padding-left: 18px;
    font-size: 13.5px;
    font-weight: 500;
    line-height: 22px;
  }
  .contact-list li {
    display: flex;
    align-items: center;
    gap: 8px;
  }
  .contact-icon { width: 12px; height: 12px; flex: none; }

  .services {
    margin-top: 52px;
    font-size: 15.5px;
    line-height: 24px;
    list-style: none;
  }
  .service-bullet {
    display: inline-block;
    width: 6px;
    height: 6px;
    border-radius: 50%;
    background: var(--accent);
    margin: 0 7px;
    vertical-align: middle;
  }

  /* Brand side */
  .card-brand {
    display: flex;
    align-items: center;
    justify-content: center;
    gap: 16px;
  }
  .brand-dot {
    width: 26px;
    height: 26px;
    border-radius: 50%;
    background: var(--accent);
  }
  .brand-name {
    font-family: "Roboto", Arial, sans-serif;
    font-weight: 400;
    font-size: 44px;
    letter-spacing: 4px;
    text-transform: uppercase;
    color: var(--text-light);
  }
</style>
</head>
<body>

  <section class="card card-info">
    <div class="identity-row">
      <div class="identity">
        <div class="identity-name">Dalton Vessey</div>
        <div class="identity-title">CEO</div>
      </div>
      <div class="divider"></div>
      <ul class="contact-list">
        <li>
          <svg class="contact-icon" viewBox="0 0 24 24" fill="var(--accent)"><path d="M6.6 10.8a15.1 15.1 0 0 0 6.6 6.6l2.2-2.2c.3-.3.7-.4 1-.2 1.1.4 2.3.6 3.6.6.6 0 1 .4 1 1V20c0 .6-.4 1-1 1A17 17 0 0 1 3 4c0-.6.4-1 1-1h3.5c.6 0 1 .4 1 1 0 1.3.2 2.5.6 3.6.1.3 0 .7-.2 1z"/></svg>
          <span>847-302-1964 (Text Me!)</span>
        </li>
        <li>
          <svg class="contact-icon" viewBox="0 0 24 24" fill="var(--accent)"><path d="M2 5h20v14H2z"/><path d="M2 5l10 8 10-8" fill="none" stroke="var(--card-bg)" stroke-width="2"/></svg>
          <span>dalton@glintharbor.example</span>
        </li>
        <li>
          <svg class="contact-icon" viewBox="0 0 24 24" fill="none" stroke="var(--accent)" stroke-width="2.4"><circle cx="12" cy="12" r="10"/><path d="M2 12h20M12 2c3 3 3 17 0 20M12 2c-3 3-3 17 0 20"/></svg>
          <span>www.glintharbor.example</span>
        </li>
      </ul>
    </div>

    <ul class="services">
      <li>Eyewear Sales<span class="service-bullet"></span>Admin Duties<span class="service-bullet"></span>Revenue Collection</li>
      <li>Leadership<span class="service-bullet"></span>Tech Adoption<span class="service-bullet"></span>COGS Reduction</li>
      <li>Product Sourcing<span class="service-bullet"></span>Medical Growth</li>
    </ul>
  </section>

  <section class="card card-brand">
    <div class="brand-dot"></div>
    <div class="brand-name">Glint Harbor</div>
  </section>

</body>
</html>
```